Biz card for my counselling/social work practice

Biz card design for my counselling practice, focus on well-being, I am a social worker who also teaches meditation and workshops but my main focus for the card is my counselling practice. My website reveals a gentle flowing quality which I would life reflected in my card. This business card will be designed to share with other practitioners who are looking for support with their clients to take their healing to another level or well-being.

Target Market(s)

professionals seeking mental health counselling/men/women/ those seeking to improve their well-being through insight based counselling to optimize their lives and process trauma or limiting patterns

Industry/Entity Type

Counsellor

Contact Information for Business Card

Info on the card: perhaps text is aligned left?
Maribel Strand, MSW, RSW
Counsellor
614.295.3140
info@maribelstrand.example
www.maribelstrand.example

Please use a modern font doesn’t need to be the one chosen below. Thank you

Font styles to use
Serif

Colors
3176b5
33a6d7
33b8a4
6b449b
abd037
d2a4cc
e55fa2

Requirements
Must have
• My business card details on front
• Backside
• Accelerated Resolution Therapy
• Cognitive Behavioral Therapy
• Mindfulness Informed Therapy
Nice to have
• I would like the card to be basic, (white or creme without too much bold colour) and with perhaps a stripe or band of vertical colour in blue or green (or a merge of colour) perhaps embossed or in a negative space. (this is one idea, but do not want the card to be too feminine or interest only women as i see men too so this is only an idea, but not 100 percent on this.
• I do not have a logo. I would prefer to heart from my website not to be used in the design as i am considering modifying this and re-branding.
Should not have
• too bold colours or bright yellow/blacks. i Like tones that are greens, blues.

```html
<!DOCTYPE html>
<html lang="en">
<head>
<meta charset="utf-8">
<title>Maribel Strand — Business Card</title>
<link rel="stylesheet" href="https://fonts.googleapis.com/css2?family=Roboto:wght@500&family=Work+Sans:wght@400;500&display=swap">
<style>
  :root {
    --backdrop: #1c1c1c;
    --paper: #efefef;
    --paper-raised: #f2f2f2;
    --violet: #6b3a9b;
    --ink: #333333;
    --rule: #8a6bb5;
    --lime: #9fd03a;
    --wash-light: #9c86c4;
    --wash-mid: #8468b2;
    --wash-deep: #5f3f8c;
    --white: #ffffff;
  }
  * { margin: 0; padding: 0; box-sizing: border-box; }
  html, body { width: 1200px; height: 897px; overflow: hidden; background: var(--backdrop); }
  .stage { position: relative; width: 1200px; height: 897px; }

  .card {
    position: absolute;
    left: 326px;
    width: 549px;
    height: 298px;
    overflow: hidden;
    box-shadow: 0 6px 14px rgba(0,0,0,0.5);
  }
  .card-front { top: 126px; background: var(--paper); }
  .card-back { top: 473px; }

  .identity { position: absolute; left: 28px; top: 154px; }
  .identity-name {
    font-family: "Roboto", sans-serif;
    font-weight: 500;
    font-size: 22px;
    color: var(--violet);
    letter-spacing: -0.2px;
    line-height: 1;
  }
  .identity-role {
    font-family: "Work Sans", sans-serif;
    font-size: 13.5px;
    color: var(--ink);
    margin-top: 4px;
    letter-spacing: 0.3px;
  }
  .identity-rule {
    width: 72px; height: 1px; background: var(--rule);
    margin-top: 14px;
  }
  .contact-list { list-style: none; margin-top: 11px; }
  .contact-item {
    display: flex; align-items: center; gap: 5px;
    font-family: "Work Sans", sans-serif;
    font-size: 14px;
    color: var(--ink);
    letter-spacing: 0.4px;
    height: 18px;
  }
  .contact-icon { width: 9px; height: 9px; flex: none; }

  .emboss-disc {
    position: absolute;
    left: 380px; top: 160px;
    width: 112px; height: 112px;
    border-radius: 50%;
    background: var(--paper-raised);
    border: 1px solid #e2e2e2;
    box-shadow: 2px 3px 4px rgba(0,0,0,0.16);
  }

  .photo-wash {
    position: absolute; inset: 0;
    background:
      radial-gradient(ellipse at 78% 50%, rgba(176,143,184,0.9) 0%, rgba(176,143,184,0) 38%),
      linear-gradient(180deg, var(--wash-light) 0%, var(--wash-mid) 55%, var(--wash-deep) 100%);
  }
  .welcome { position: absolute; left: 29px; top: 124px; color: var(--white); }
  .welcome-title {
    font-family: "Roboto", sans-serif;
    font-weight: 500;
    font-size: 25.5px;
    letter-spacing: 1.7px;
    line-height: 1;
  }
  .welcome-sub {
    font-family: "Work Sans", sans-serif;
    font-size: 14.3px;
    letter-spacing: 0.6px;
    margin-top: 7px;
  }
  .service-list { list-style: none; position: absolute; left: 29px; top: 202px; }
  .service-item {
    display: flex; align-items: center; gap: 9px;
    font-family: "Work Sans", sans-serif;
    font-size: 14.5px;
    color: var(--white);
    letter-spacing: 0.9px;
    height: 23px;
  }
  .service-mark { width: 10px; height: 10px; background: var(--lime); flex: none; }
</style>
</head>
<body>
<main class="stage">
  <section class="card card-front">
    <div class="identity">
      <h1 class="identity-name">Maribel Strand, MSW, RSW</h1>
      <p class="identity-role">Counsellor</p>
      <div class="identity-rule"></div>
      <ul class="contact-list">
        <li class="contact-item">
          <svg class="contact-icon" viewBox="0 0 10 10"><path d="M2 1 L4 1 L4.6 3 L3.4 3.8 Q4.3 5.8 6.2 6.6 L7 5.4 L9 6 L9 8 Q8.5 9 7.5 9 Q2.5 8 1 2.5 Q1 1.5 2 1 Z" fill="var(--violet)"/></svg>
          614.295.3140
        </li>
        <li class="contact-item">
          <svg class="contact-icon" viewBox="0 0 10 10"><rect x="0.8" y="2" width="8.4" height="6" fill="none" stroke="var(--violet)" stroke-width="1.1"/><path d="M1 2.3 L5 5.3 L9 2.3" fill="none" stroke="var(--violet)" stroke-width="1.1"/></svg>
          info@maribelstrand.example
        </li>
        <li class="contact-item">
          <svg class="contact-icon" viewBox="0 0 10 10"><circle cx="5" cy="5" r="4" fill="none" stroke="var(--violet)" stroke-width="1"/><ellipse cx="5" cy="5" rx="1.8" ry="4" fill="none" stroke="var(--violet)" stroke-width="0.8"/><path d="M1 5 H9" stroke="var(--violet)" stroke-width="0.8"/></svg>
          www.maribelstrand.example
        </li>
      </ul>
    </div>
    <div class="emboss-disc" aria-hidden="true"></div>
  </section>

  <section class="card card-back">
    <div class="photo-wash" role="img" aria-label="Photograph of the counsellor outdoors, with a meadow and trees behind, tinted in violet"></div>
    <div class="welcome">
      <h2 class="welcome-title">A WARM WELCOME</h2>
      <p class="welcome-sub">Therapy, Coaching, Yoga &amp; Health</p>
    </div>
    <ul class="service-list">
      <li class="service-item"><span class="service-mark"></span>Accelerated Resolution Therapy</li>
      <li class="service-item"><span class="service-mark"></span>Cognitive Behavioral Therapy</li>
      <li class="service-item"><span class="service-mark"></span>Mindfulness Informed Therapy</li>
    </ul>
  </section>
</main>
</body>
</html>
```